Certificate of Completion - Educational Trainings

We are looking for a certificate of completion for individuals who complete one of our specific trainings. Files should be provided in a Word (docx) or PowerPoint (pptx) format. The "Talmoray example.png" file is to show necessary information. Copies of logos have been included for design purposes.

Target Market(s)

Training Participants

Industry/Entity Type

Healthcare

Font styles to use
Sans Serif

```html
<!DOCTYPE html>
<html lang="en">
<head>
<meta charset="utf-8">
<title>Talmoray Certificate of Completion</title>
<link href="https://fonts.googleapis.com/css2?family=Cinzel:wght@400;500&family=Montserrat:wght@400;500;600;800&family=Alex+Brush&display=swap" rel="stylesheet">
<style>
  :root {
    --backdrop: #e4e6e4;
    --green: #5cb146;
    --green-dark: #2f8a3a;
    --green-soft: #a9d69a;
    --ink: #161616;
    --paper: #ffffff;
    --rule: #b98a6a;
    --divider: #dddddd;
  }
  * { margin: 0; padding: 0; box-sizing: border-box; }
  html, body { width: 1200px; height: 1200px; overflow: hidden; }
  body {
    background: var(--backdrop);
    font-family: "Montserrat", sans-serif;
    color: var(--ink);
    position: relative;
  }
  .certificate {
    position: absolute;
    left: 50px; top: 200px;
    width: 1100px; height: 800px;
    background: var(--green);
    padding: 22px;
  }
  .sheet {
    position: relative;
    width: 100%; height: 100%;
    background: var(--paper);
  }
  .frame-line {
    position: absolute;
    inset: 12px;
    border: 3px double var(--green);
  }
  .border-ornament {
    position: absolute;
    inset: 24px;
    border: 26px solid var(--green-soft);
  }
  .content {
    position: absolute;
    inset: 50px;
    padding: 14px 40px 14px;
    display: flex;
    flex-direction: column;
    align-items: center;
    text-align: center;
  }
  .brand {
    margin-top: 6px;
    display: flex; align-items: center; justify-content: center; gap: 16px;
  }
  .brand-dot {
    width: 44px; height: 44px; border-radius: 50%;
    background: var(--green-dark);
  }
  .brand-name {
    font-weight: 800; font-size: 54px; letter-spacing: 4px; line-height: 1;
    color: var(--ink);
  }
  .brand-address {
    margin-top: 8px;
    font-size: 14px; font-weight: 500; line-height: 1.3;
    text-transform: uppercase; letter-spacing: 0.5px;
  }
  .title {
    margin-top: 12px;
    font-family: "Cinzel", serif;
    font-weight: 400;
    font-size: 108px; line-height: 1;
    color: var(--green);
    letter-spacing: 2px;
  }
  .subtitle {
    margin-top: 6px;
    font-size: 21px; font-weight: 500; color: var(--green);
    letter-spacing: 1px;
  }
  .awarded {
    margin-top: 6px;
    font-size: 21px; font-weight: 600; letter-spacing: 1.5px;
  }
  .divider {
    width: 560px; height: 1px; background: var(--divider);
  }
  .divider-top { margin-top: 8px; }
  .divider-bottom { margin-bottom: 8px; }
  .recipient {
    font-family: "Alex Brush", cursive;
    font-size: 68px; line-height: 1.1;
  }
  .course {
    font-size: 16px; font-weight: 500; text-transform: uppercase;
    line-height: 1.4; letter-spacing: 0.5px;
  }
  .signoffs {
    margin-top: auto;
    width: 100%;
    display: flex; justify-content: space-between; align-items: flex-end;
    padding: 0 70px;
  }
  .signoff { width: 230px; text-align: center; }
  .signoff-script {
    font-family: "Alex Brush", cursive;
    font-size: 32px; color: var(--green); line-height: 1.1;
  }
  .signoff-rule { height: 2px; background: var(--rule); margin: 2px 0 6px; }
  .signoff-label { font-size: 18px; font-weight: 500; text-transform: uppercase; line-height: 1.2; }
  .seal { width: 60px; height: 90px; }
  .footnote {
    margin-top: 14px;
    font-size: 9.5px; text-transform: uppercase; letter-spacing: 0.3px; line-height: 1.2;
  }
</style>
</head>
<body>
  <main class="certificate">
    <div class="sheet">
      <div class="frame-line"></div>
      <div class="border-ornament" role="img" aria-label="Decorative green interlaced border pattern with leaf corners"></div>
      <div class="content">
        <header class="brand">
          <span class="brand-dot"></span>
          <span class="brand-name">TALMORAY</span>
        </header>
        <p class="brand-address">48 Harbor Lane, Ste 310 Brookfield, VT 05036<br>Education Registry Sponsor Number 71208</p>
        <h1 class="title">CERTIFICATE</h1>
        <p class="subtitle">OF COMPLETION</p>
        <p class="awarded">THIS CERTIFICATE IS AWARDED TO</p>
        <div class="divider divider-top"></div>
        <p class="recipient">Mara Ellison</p>
        <div class="divider divider-bottom"></div>
        <p class="course">For successful completion of<br>Best Practices: Budget Process/Budget Building Complete<br>Online Field of Study Finance CPE Credits: 1</p>
        <div class="signoffs">
          <div class="signoff">
            <p class="signoff-script">05/16/2024</p>
            <div class="signoff-rule"></div>
            <p class="signoff-label">Completion Date</p>
          </div>
          <svg class="seal" viewBox="0 0 64 96" role="img" aria-label="Award seal">
            <path d="M20 50 L10 92 L22 84 L30 94 L32 54 Z" fill="#2f8a3a"/>
            <path d="M44 50 L54 92 L42 84 L34 94 L32 54 Z" fill="#2f8a3a"/>
            <circle cx="32" cy="32" r="30" fill="#2f8a3a"/>
            <circle cx="32" cy="32" r="20" fill="#ffffff"/>
          </svg>
          <div class="signoff">
            <p class="signoff-script">Jana Holt</p>
            <div class="signoff-rule"></div>
            <p class="signoff-label">Senior Consultant</p>
          </div>
        </div>
        <p class="footnote">In accordance with the standard of the Continuing Education Registry, CPE credits have been granted based on a 50 minute hour.</p>
      </div>
    </div>
  </main>
</body>
</html>
```